Core Investment Strategy's Super Pie Chart

We need a one page visual explanation of an investment strategy we call "Hollis/Varrowby". This strategy emphasizes a "core" portfolio that will seldom change and "perimeter" investments that will change. Our investment management firm caters to wealthy individuals. We want to project an image of strength and reliability. At the same time, we are willing to explore new concepts. I have uploaded a PDF of my graphically-challenged assistant's attempt at creating the one page visual.

Investment

```html
<!DOCTYPE html>
<html lang="en">
<head>
<meta charset="utf-8">
<title>Hollis/Varrowby Portfolio</title>
<link href="https://fonts.googleapis.com/css2?family=Carlito:wght@400;700&display=swap" rel="stylesheet">
<style>
  :root {
    --stage: #d4d6d9;
    --slide-center: #ffffff;
    --slide-edge: #d9dadc;
    --title-fill: #4a7ebb;
    --title-text: #ffffff;
    --label: #222222;
    --outer-alt: #1f3864;
    --outer-alt-dark: #15284a;
    --outer-funds: #e31414;
    --outer-funds-dark: #a50d0d;
    --outer-core: #5b8a2e;
    --outer-core-dark: #3f6420;
    --outer-other: #8e56a8;
    --lg-cap: #1778cc;
    --mid-cap: #1766b0;
    --sm-cap: #2390e0;
    --intl: #27b6f0;
    --short-bonds: #96d03f;
    --inter-bonds: #70ac2c;
    --inner-side-blue: #0e4f8c;
    --inner-side-cyan: #1585b5;
  }
  html, body {
    margin: 0;
    width: 1200px;
    height: 674px;
    overflow: hidden;
    background: var(--stage);
  }
  .slide {
    position: absolute;
    left: 150px;
    top: 0;
    width: 899px;
    height: 674px;
    background: radial-gradient(ellipse at 50% 45%, var(--slide-center) 0%, #f3f3f4 45%, var(--slide-edge) 100%);
    font-family: "Carlito", "Calibri", sans-serif;
  }
  .slide svg { display: block; width: 899px; height: 674px; }
  .title-box { fill: var(--title-fill); }
  .title-text { fill: var(--title-text); font-size: 10px; font-weight: 700; }
  .pie-label { fill: var(--label); font-size: 6.2px; }
  .legend-text { fill: var(--label); font-size: 5px; }
</style>
</head>
<body>
<main class="slide">
  <svg viewBox="0 0 484 362" aria-label="Hollis/Varrowby Portfolio pie chart">
    <defs>
      <filter id="soft-shadow" x="-20%" y="-20%" width="140%" height="140%">
        <feGaussianBlur stdDeviation="3"/>
      </filter>
    </defs>

    <g class="chart-title">
      <rect class="title-box" x="151" y="34" width="178" height="28"/>
      <text class="title-text" x="240" y="52" text-anchor="middle">Hollis/Varrowby Portfolio</text>
    </g>

    <g class="perimeter-ring">
      <path fill="var(--outer-funds-dark)" d="M347,171 A104,74 0 0 1 243,245 L243,275 A104,74 0 0 0 347,201 Z"/>
      <path fill="var(--outer-core-dark)" d="M243,245 A104,74 0 0 1 139,171 L139,201 A104,74 0 0 0 243,275 Z"/>
      <path fill="var(--outer-alt)" d="M243,171 L243,97 A104,74 0 0 1 347,171 Z"/>
      <path fill="var(--outer-funds)" d="M243,171 L347,171 A104,74 0 0 1 243,245 Z"/>
      <path fill="var(--outer-core)" d="M243,171 L243,245 A104,74 0 0 1 139,171 Z"/>
      <path fill="var(--outer-other)" d="M243,171 L139,171 A104,74 0 0 1 243,97 Z"/>
    </g>

    <ellipse cx="244" cy="165" rx="78" ry="55" fill="rgba(0,0,0,0.35)" filter="url(#soft-shadow)"/>

    <g class="core-pie">
      <path fill="var(--inner-side-blue)" d="M315,150 A74,53 0 0 1 241,203 L241,213 A74,53 0 0 0 315,160 Z"/>
      <path fill="var(--inner-side-cyan)" d="M241,203 A74,53 0 0 1 167,150 L167,160 A74,53 0 0 0 241,213 Z"/>
      <path fill="var(--lg-cap)" d="M241,150 L241,97 A74,53 0 0 1 293.3,187.5 Z"/>
      <path fill="var(--mid-cap)" d="M241,150 L293.3,187.5 A74,53 0 0 1 269.3,199 Z"/>
      <path fill="var(--sm-cap)" d="M241,150 L269.3,199 A74,53 0 0 1 241,203 Z"/>
      <path fill="var(--intl)" d="M241,150 L241,203 A74,53 0 0 1 188.7,187.5 Z"/>
      <path fill="var(--short-bonds)" d="M241,150 L188.7,187.5 A74,53 0 0 1 167,150 Z"/>
      <path fill="var(--inter-bonds)" d="M241,150 L167,150 A74,53 0 0 1 241,97 Z"/>
    </g>

    <g class="pie-labels">
      <text class="pie-label" x="132" y="125" text-anchor="end">Other, 2%</text>
      <text class="pie-label" x="345" y="125">Alternative Assets, 7%</text>
      <text class="pie-label" x="131" y="205" text-anchor="end">Attractive Core</text>
      <text class="pie-label" x="131" y="214" text-anchor="end">Assets, 3%</text>
      <text class="pie-label" x="352" y="212">Funds, 8%</text>
    </g>

    <g class="legend">
      <rect x="128" y="305" width="3" height="3" fill="var(--inter-bonds)"/>
      <text class="legend-text" x="133" y="308">Intermediate Bonds, 20%</text>
      <rect x="207" y="305" width="3" height="3" fill="var(--short-bonds)"/>
      <text class="legend-text" x="212" y="308">Short-Term Bonds, 10%</text>
      <rect x="282" y="305" width="3" height="3" fill="var(--lg-cap)"/>
      <text class="legend-text" x="287" y="308">Lg. Cap Equities, 30%</text>

      <rect x="129" y="317" width="3" height="3" fill="var(--mid-cap)"/>
      <text class="legend-text" x="134" y="320">Mid Cap Equities, 5%</text>
      <rect x="205" y="317" width="3" height="3" fill="var(--sm-cap)"/>
      <text class="legend-text" x="210" y="320">Sm. Cap Equities, 5%</text>
      <rect x="281" y="317" width="3" height="3" fill="var(--intl)"/>
      <text class="legend-text" x="286" y="320">Int'l/Dev. Equities, 10%</text>
    </g>
  </svg>
</main>
</body>
</html>
```